Our new beauty salon requires a price list brochure

Our beauty clinic is a medical grade skin care clinic. So our salon is very clinical and professional in appearance. I would like the colours to be similar to our logo design with some nice texture or abstract shapes thrown in.
Pricelist, contact details and logo is attached
I would prefer it to be a 3 fold brochure.

Target Market(s)

Females aged 30-50

Colors
85acd3
cedeed
c4c4c4
5c5c5c
000000
ffffff
eea3c7
f9d9e8
dbdbdb

Requirements
Must have
• easy to read

```html
<!DOCTYPE html>
<html lang="en">
<head>
<meta charset="utf-8">
<title>Elara Aesthetics – Price List Brochure</title>
<link href="https://fonts.googleapis.com/css2?family=Raleway:wght@300;400;600;700&display=swap" rel="stylesheet">
<style>
:root{
  --page:#e6e6e6;
  --ink:#5c5c5c;
  --dark:#333333;
  --green:#8cc63f;
  --green-dark:#6fa82b;
  --blue:#85acd3;
  --blue-light:#cedeed;
  --pink:#eea3c7;
  --pink-light:#f9d9e8;
  --white:#ffffff;
  --rule:#dbdbdb;
}
*{box-sizing:border-box;margin:0;padding:0}
html,body{width:835px;height:1200px;overflow:hidden}
body{background:var(--page);font-family:"Raleway",sans-serif;color:var(--ink);position:relative}
.spread{position:absolute;left:22px;width:791px;height:560px;overflow:hidden;
  background:radial-gradient(ellipse at 30% 40%,#f4f8fc 0%,#dfeaf5 55%,#c9dcee 100%);
  box-shadow:0 6px 16px rgba(0,0,0,.25)}
.spread.outer{top:22px}
.spread.inner{top:612px}
.bokeh{position:absolute;inset:0;width:100%;height:100%}
.fold{position:absolute;top:0;bottom:0;width:1px;background:rgba(133,172,211,.35)}
.panel{position:absolute;top:0;height:100%;width:263px;padding:16px 18px}
.p1{left:0}.p2{left:264px}.p3{left:528px}
.heading{font-weight:700;font-size:11px;letter-spacing:.5px;color:var(--dark);text-transform:uppercase;margin:0 0 7px;display:flex;align-items:center;gap:5px}
.heading .tag{background:var(--green);color:var(--white);font-size:8px;padding:1px 3px}
.price-list{display:flex;flex-direction:column;gap:3px;margin-bottom:9px;width:172px}
.row{display:flex;height:12px;font-size:7.5px;line-height:12px}
.row .item{flex:1;background:var(--white);padding:0 5px;white-space:nowrap;overflow:hidden}
.row .price{width:40px;background:var(--green);color:var(--white);font-weight:600;text-align:center}
.row.feature .item{background:var(--green-dark);color:var(--white)}
.row.feature .price{background:var(--blue)}
.wide .price-list{width:226px}
.note{font-size:7px;line-height:1.35;background:var(--white);padding:3px 5px;margin:-6px 0 9px;width:226px}
.contact{position:absolute;left:18px;right:18px;top:330px;text-align:center;font-size:7.5px;line-height:1.55}
.contact .name{font-weight:700;font-size:11px;letter-spacing:1px;color:var(--dark);margin-bottom:6px}
.wordmark{position:absolute;top:24px;right:28px;font-weight:300;font-size:26px;letter-spacing:2px;color:var(--blue)}
.photo{position:absolute}
.photo.portrait{right:0;top:70px;width:225px;height:490px;border-radius:110px 0 0 0;
  background:linear-gradient(160deg,#d9c2b3 0%,#e9d6c9 45%,#cfdcec 100%)}
.photo.legs{left:0;bottom:0;width:263px;height:110px;
  background:linear-gradient(90deg,#e8dcd3 0%,#f1e7e0 50%,#dbe7f2 100%)}
.photo.smile{right:0;bottom:0;width:263px;height:170px;border-radius:90px 0 0 0;
  background:linear-gradient(150deg,#d8bfae 0%,#ecdacd 55%,#d5e2f0 100%)}
.treatment{font-size:7px;line-height:1.4;margin-bottom:6px;width:226px}
.treatment b{color:var(--green-dark);font-weight:700}
.treatment .lead{color:var(--dark);font-weight:600}
</style>
</head>
<body>

<section class="spread outer" aria-label="Brochure outer side">
  <svg class="bokeh" viewBox="0 0 791 560" aria-hidden="true">
    <g fill="#ffffff" opacity=".35">
      <circle cx="80" cy="470" r="22"/><circle cx="220" cy="90" r="14"/><circle cx="360" cy="260" r="30"/>
      <circle cx="470" cy="480" r="18"/><circle cx="560" cy="160" r="12"/><circle cx="320" cy="500" r="10"/>
    </g>
  </svg>
  <span class="fold" style="left:263px"></span><span class="fold" style="left:527px"></span>

  <div class="panel p1">
    <h2 class="heading"><span class="tag">IPL</span>Hair Removal</h2>
    <div class="price-list">
      <div class="row"><span class="item">Upper Lip</span><span class="price">$39</span></div>
      <div class="row"><span class="item">Chin</span><span class="price">$39</span></div>
      <div class="row"><span class="item">Cheeks</span><span class="price">$49</span></div>
      <div class="row"><span class="item">Whole Face</span><span class="price">$99</span></div>
    </div>
    <div class="price-list">
      <div class="row"><span class="item">Bikini</span><span class="price">$69</span></div>
      <div class="row"><span class="item">G-String</span><span class="price">$89</span></div>
      <div class="row"><span class="item">Brazilian</span><span class="price">$109</span></div>
    </div>
    <div class="price-list">
      <div class="row"><span class="item">Underarms</span><span class="price">$49</span></div>
      <div class="row"><span class="item">Half Arm</span><span class="price">$79</span></div>
      <div class="row"><span class="item">Full Arm</span><span class="price">$119</span></div>
      <div class="row"><span class="item">Half Leg</span><span class="price">$129</span></div>
      <div class="row"><span class="item">Thighs</span><span class="price">$139</span></div>
      <div class="row"><span class="item">Full Leg</span><span class="price">$219</span></div>
    </div>
    <div class="price-list">
      <div class="row"><span class="item">Full Back</span><span class="price">$189</span></div>
      <div class="row"><span class="item">Shoulders</span><span class="price">$99</span></div>
      <div class="row"><span class="item">Nipples</span><span class="price">$39</span></div>
      <div class="row"><span class="item">Small Trail</span><span class="price">$39</span></div>
      <div class="row"><span class="item">Stomach</span><span class="price">$89</span></div>
      <div class="row"><span class="item">Chest</span><span class="price">$119</span></div>
      <div class="row"><span class="item">Buttocks</span><span class="price">$119</span></div>
    </div>
  </div>

  <div class="panel p2">
    <h2 class="heading"><span class="tag">IPL</span>Photo Rejuvenation</h2>
    <div class="price-list">
      <div class="row"><span class="item">Full Face</span><span class="price">$199</span></div>
      <div class="row"><span class="item">Neck</span><span class="price">$149</span></div>
      <div class="row"><span class="item">Face, neck and décolletage</span><span class="price">$349</span></div>
      <div class="row"><span class="item">Back of Hands</span><span class="price">$129</span></div>
    </div>
    <h2 class="heading" style="margin-top:16px">Tinting</h2>
    <div class="price-list">
      <div class="row"><span class="item">Eyebrow Tint</span><span class="price">$15</span></div>
      <div class="row"><span class="item">Lash Lift and Tint</span><span class="price">$79</span></div>
      <div class="row"><span class="item">Eyebrow wax and tint</span><span class="price">$35</span></div>
      <div class="row"><span class="item">Eyebrow and Lash Tint</span><span class="price">$35</span></div>
    </div>
    <address class="contact" style="font-style:normal">
      <p class="name">ELARA AESTHETICS</p>
      <p>14/220 Harbour Drive</p>
      <p>Glenwood Park</p>
      <p>Western Australia</p>
      <p style="margin-top:6px">T: (08) 5550 1827</p>
      <p>hello@elaraclinic.com</p>
      <p>www.elaraclinic.com</p>
      <p style="margin-top:6px">@elara_aesthetics</p>
    </address>
  </div>

  <div class="panel p3">
    <p class="wordmark">elara aesthetics</p>
    <div class="photo portrait" role="img" aria-label="Portrait of a woman with clear glowing skin, hand resting on her cheek"></div>
  </div>
</section>

<section class="spread inner" aria-label="Brochure inner side">
  <svg class="bokeh" viewBox="0 0 791 560" aria-hidden="true">
    <g fill="#ffffff" opacity=".35">
      <circle cx="230" cy="60" r="18"/><circle cx="400" cy="330" r="26"/><circle cx="600" cy="240" r="16"/>
      <circle cx="740" cy="90" r="20"/><circle cx="150" cy="300" r="12"/>
    </g>
  </svg>
  <span class="fold" style="left:263px"></span><span class="fold" style="left:527px"></span>

  <div class="panel p1">
    <h2 class="heading">Waxing</h2>
    <div class="price-list">
      <div class="row"><span class="item">Eyebrow</span><span class="price">$22</span></div>
      <div class="row"><span class="item">Lip</span><span class="price">$15</span></div>
      <div class="row"><span class="item">Chin</span><span class="price">$15</span></div>
      <div class="row"><span class="item">Sides of Face</span><span class="price">$20</span></div>
      <div class="row"><span class="item">Underarm</span><span class="price">$22</span></div>
      <div class="row"><span class="item">Half Arm</span><span class="price">$29</span></div>
      <div class="row"><span class="item">Full Arm</span><span class="price">$39</span></div>
      <div class="row"><span class="item">Fingers</span><span class="price">$10</span></div>
      <div class="row"><span class="item">Full Face</span><span class="price">$49</span></div>
      <div class="row"><span class="item">Upper Leg</span><span class="price">$35</span></div>
      <div class="row"><span class="item">Lower Leg</span><span class="price">$35</span></div>
      <div class="row"><span class="item">Full Leg</span><span class="price">$55</span></div>
      <div class="row"><span class="item">Inner Thigh</span><span class="price">$20</span></div>
      <div class="row"><span class="item">Full Back</span><span class="price">$45</span></div>
      <div class="row"><span class="item">Bikini</span><span class="price">$29</span></div>
      <div class="row"><span class="item">G-String</span><span class="price">$45</span></div>
      <div class="row"><span class="item">Brazilian</span><span class="price">$59</span></div>
    </div>
    <div class="price-list">
      <div class="row"><span class="item">Eyebrow Wax and Lip</span><span class="price">$35</span></div>
      <div class="row"><span class="item">Eyebrow, Lip and Chin</span><span class="price">$45</span></div>
    </div>
    <div class="photo legs" role="img" aria-label="Smooth bare legs resting on a soft surface"></div>
  </div>

  <div class="panel p2 wide">
    <h2 class="heading">Men's Waxing</h2>
    <div class="price-list">
      <div class="row"><span class="item">Nose Hair</span><span class="price">$15</span></div>
      <div class="row"><span class="item">Eyebrow</span><span class="price">$25</span></div>
      <div class="row"><span class="item">Back</span><span class="price">$55</span></div>
      <div class="row"><span class="item">Full Back</span><span class="price">$69</span></div>
      <div class="row"><span class="item">Chest and Abdomen</span><span class="price">$59</span></div>
    </div>
    <div class="price-list">
      <div class="row feature"><span class="item">Smooth Pack</span><span class="price">$99</span></div>
      <div class="row feature"><span class="item">Brow &amp; Lash Pack</span><span class="price">$59</span></div>
      <div class="row feature"><span class="item">Legs &amp; Bikini Pack</span><span class="price">$79</span></div>
      <div class="row feature"><span class="item">Full Body Pack</span><span class="price">$149</span></div>
    </div>
    <p class="note">Choose any three areas from brow, lip, chin or underarm and save on every visit.</p>
    <div class="price-list">
      <div class="row"><span class="item">Brazilian and Underarm</span><span class="price">$69</span></div>
      <div class="row"><span class="item">Full Leg and Brazilian</span><span class="price">$99</span></div>
    </div>
    <h2 class="heading" style="margin-top:10px">Chemical <span style="color:var(--green-dark)">Peels</span></h2>
    <div class="price-list">
      <div class="row"><span class="item">Glycolic 30% Peel</span><span class="price">$99</span></div>
      <div class="row"><span class="item">Lactic Acid Peel</span><span class="price">$119</span></div>
      <div class="row"><span class="item">Age Defying Peel</span><span class="price">$139</span></div>
      <div class="row"><span class="item">Brightening Peel</span><span class="price">$129</span></div>
      <div class="row"><span class="item">Pigment Peel</span><span class="price">$149</span></div>
    </div>
  </div>

  <div class="panel p3 wide">
    <div class="price-list">
      <div class="row"><span class="item">Cosmetic Peel</span><span class="price">$89</span></div>
      <div class="row"><span class="item">Microdermabrasion</span><span class="price">$99</span></div>
      <div class="row"><span class="item">Hydrating Facial</span><span class="price">$109</span></div>
      <div class="row"><span class="item">Express Facial</span><span class="price">$69</span></div>
    </div>
    <h2 class="heading" style="margin-top:8px">Lumina LED</h2>
    <p class="treatment"><b>$90</b> <span class="lead">per treatment</span> – gentle light therapy to calm, repair and renew the skin.</p>
    <p class="treatment"><b>$350</b> <span class="lead">Rejuvenation</span> – course of five sessions for firmer skin.</p>
    <p class="treatment"><b>$350</b> <span class="lead">Clear Skin</span> – course of five sessions for blemish-prone skin.</p>
    <p class="treatment"><b>$250</b> <span class="lead">Recovery</span> – three sessions after peels or laser.</p>
    <div class="photo smile" role="img" aria-label="Smiling woman with radiant skin"></div>
  </div>
</section>

</body>
</html>
```